Website for an interior designer

We need a new website for Rosa Lynn Thackery whose new business name is Rosa Lynn Thackery Interiors. She is a residential interior designer with a mix of modern and contemporary tastes. We are in the process of overhauling her website which is +15 years old and not an accurate reflection of her tastes. The uploaded photos are from some of the houses she has done as well as her logo(s). We would need a section for "About Us" that would have a paragraph of text and bullets showing services and a gallery for photos (~12 total, more to come). A contract page would be optional. The client likes the feel/look of this website: https://www.corvenhollowdesign.example/ but doesn't want to copy it exactly.

Target Market(s)

Upscale home owners

Industry/Entity Type

Interior Design

Coding

Coded - Design and coding required

Number of Pages Required

4 page

Colors

Designer to choose only greyscale colors for use in the design.

Requirements
Must have
• Home page, about us page, gallery page, contact us page.

```html
<!DOCTYPE html>
<html lang="en">
<head>
<meta charset="utf-8">
<title>Rosa Lynn Thackery Interiors</title>
<link rel="stylesheet" href="https://fonts.googleapis.com/css2?family=Playfair+Display:wght@400&family=Roboto:wght@400&family=Questrial&display=swap">
<style>
  :root {
    --ink: #2f2f2f;
    --text: #555555;
    --muted: #9a9a9a;
    --panel: #7a7a7a;
    --disc: rgba(104, 104, 104, 0.92);
    --white: #ffffff;
    --footer: #e6e6e6;
    --black: #000000;
    --line: #6a6a6a;
  }
  * { margin: 0; padding: 0; box-sizing: border-box; }
  html, body { width: 1200px; height: 3378px; overflow: hidden; background: var(--white); }
  body { position: relative; font-family: "Roboto", sans-serif; color: var(--text); }
  .abs { position: absolute; }

  /* Header */
  .site-header { position: absolute; left: 0; top: 0; width: 1200px; height: 106px; background: var(--white); }
  .brand { position: absolute; left: 50px; top: 30px; display: flex; align-items: center; gap: 12px; }
  .brand-mark { width: 40px; height: 40px; border: 1.5px solid var(--ink); border-radius: 50%; }
  .brand-name { font-family: "Playfair Display", serif; font-size: 19px; color: var(--ink); letter-spacing: 1px; line-height: 1.15; text-transform: uppercase; }
  .main-nav { position: absolute; top: 38px; left: 0; width: 1200px; font-family: "Questrial", sans-serif; font-size: 16px; color: var(--text); }
  .main-nav a { position: absolute; color: inherit; text-decoration: none; letter-spacing: 0.5px; }
  .main-nav a.current { color: var(--ink); }
  .main-nav .sep { position: absolute; top: 2px; width: 1px; height: 18px; background: #bbbbbb; }

  /* Hero */
  .hero { position: absolute; left: 0; top: 106px; width: 1200px; height: 594px;
    background: linear-gradient(100deg, #e9e9e7 0%, #d8d9d8 30%, #bfc2c3 55%, #dcdddc 75%, #f1f1ef 100%); }
  .hero-disc { position: absolute; left: 101px; top: 96px; width: 388px; height: 388px; border-radius: 50%; background: var(--disc);
    display: flex; flex-direction: column; align-items: center; justify-content: center; color: var(--white); text-align: center; }
  .hero-kicker { font-family: "Playfair Display", serif; font-size: 23px; letter-spacing: 3px; margin-bottom: 2px; }
  .hero-title { font-family: "Playfair Display", serif; font-size: 51px; line-height: 58px; }
  .hero-arrow { position: absolute; top: 250px; }

  /* About */
  .about-mark { position: absolute; left: 111px; top: 840px; width: 400px; text-align: center;
    font-family: "Playfair Display", serif; font-size: 62px; line-height: 72px; color: #3e3e3e; }
  .about-title { position: absolute; left: 581px; top: 818px; font-family: "Playfair Display", serif; font-size: 34px; line-height: 35px; color: var(--ink); }
  .about-title .light { color: var(--muted); }
  .rule { position: absolute; height: 2px; background: var(--ink); }
  .about-copy { position: absolute; left: 581px; top: 928px; width: 548px; font-size: 15.5px; line-height: 27.5px; color: var(--text); text-align: justify; }

  /* Services */
  .services { position: absolute; left: 0; top: 1221px; width: 1200px; height: 539px;
    background: linear-gradient(90deg, #d9d6cf 0%, #ebe8e2 35%, #cfc9bd 60%, #e2ded6 100%); }
  .services-panel { position: absolute; left: 0; top: 0; }
  .services-title { position: absolute; left: 660px; top: 88px; font-family: "Playfair Display", serif; font-size: 36px; color: var(--white); }
  .service-list { position: absolute; left: 660px; top: 168px; list-style: none; color: var(--white); font-size: 16.5px; }
  .service-list li { height: 45.6px; display: flex; align-items: center; gap: 12px; }

  /* Gallery */
  .gallery-title { position: absolute; left: 0; top: 1806px; width: 1200px; text-align: center; font-family: "Playfair Display", serif; font-size: 36px; color: var(--ink); }
  .gallery-title .light { color: var(--muted); }
  .gallery-grid { position: absolute; left: 88px; top: 1898px; display: grid; grid-template-columns: repeat(4, 248px); grid-auto-rows: 187px; column-gap: 10px; row-gap: 10px; }
  .tile { width: 248px; height: 187px; }
  .btn-outline { position: absolute; left: 505px; top: 2518px; width: 186px; height: 54px; border: 2px solid #777777;
    display: flex; align-items: center; justify-content: center; font-family: "Questrial", sans-serif; font-size: 19px; color: var(--ink); letter-spacing: 0.5px; }

  /* Contact */
  .contact { position: absolute; left: 0; top: 2635px; width: 1200px; height: 535px;
    background: linear-gradient(100deg, #3b3b3b 0%, #555555 40%, #4a4a4a 70%, #3f3f3f 100%); }
  .contact-title { position: absolute; left: 0; top: 2692px; width: 1200px; text-align: center; font-family: "Playfair Display", serif; font-size: 36px; color: var(--white); }
  .field { position: absolute; background: var(--white); font-size: 14.5px; color: #666666; padding: 16px 19px; }
  .btn-submit { position: absolute; left: 505px; top: 3049px; width: 184px; height: 54px; background: var(--black); color: var(--white);
    display: flex; align-items: center; justify-content: center; font-family: "Questrial", sans-serif; font-size: 21px; letter-spacing: 0.5px; }

  /* Footer */
  .site-footer { position: absolute; left: 0; top: 3170px; width: 1200px; height: 208px; background: var(--footer); }
  .footer-nav a { position: absolute; top: 42px; font-family: "Questrial", sans-serif; font-size: 16px; color: #4a4a4a; text-decoration: none; }
  .copyright { position: absolute; left: 0; top: 78px; width: 1200px; text-align: center; font-size: 14.5px; color: #666666; }
  .social { position: absolute; top: 118px; width: 40px; height: 40px; border: 1.5px solid #8a8a8a; border-radius: 50%; }
</style>
</head>
<body>

<header class="site-header">
  <div class="brand">
    <span class="brand-mark"></span>
    <span class="brand-name">Rosa Lynn Thackery<br>Interiors</span>
  </div>
  <nav class="main-nav">
    <a class="current" style="left:494px">HOME</a>
    <span class="sep" style="left:582px"></span>
    <a style="left:619px">ABOUT US</a>
    <span class="sep" style="left:738px"></span>
    <a style="left:775px">SERVICES</a>
    <span class="sep" style="left:886px"></span>
    <a style="left:925px">GALLERY</a>
    <span class="sep" style="left:1029px"></span>
    <a style="left:1069px">CONTACT</a>
  </nav>
</header>

<section class="hero" role="img" aria-label="Bright white kitchen with marble counters, range hood and grey cabinets">
  <div class="hero-disc">
    <div class="hero-kicker">WELCOME TO</div>
    <div class="hero-title">ROSA LYNN<br>THACKERY</div>
  </div>
  <svg class="hero-arrow" style="left:30px" width="26" height="48" viewBox="0 0 26 48"><path d="M22 4 L4 24 L22 44" fill="none" stroke="#222" stroke-width="2"/></svg>
  <svg class="hero-arrow" style="left:1132px" width="26" height="48" viewBox="0 0 26 48"><path d="M4 4 L22 24 L4 44" fill="none" stroke="#222" stroke-width="2"/></svg>
</section>

<section class="about">
  <div class="about-mark">Rosa Lynn<br>Thackery<br>Interiors</div>
  <h2 class="about-title"><span class="light">ABOUT</span> ROSA LYNN<br>THACKERY</h2>
  <div class="rule" style="left:581px; top:900px; width:46px;"></div>
  <p class="about-copy">Rosa Lynn Thackery has extensive experience in all aspects of interior design. She has worked on a wide array of residential and commercial projects in her hometown of Houston and across the United States. Rosa Lynn’s taste can best be described as a sophisticated blend of modern and traditional styles that combine to create a clean, timeless space.</p>
</section>

<section class="services">
  <div class="abs" style="left:0;top:0;width:600px;height:539px" role="img" aria-label="Light living room with white sofas, brass coffee table and steel-framed glass doors"></div>
  <svg class="services-panel" width="1200" height="539" viewBox="0 0 1200 539">
    <path d="M505 0 C565 60 605 190 597 290 C590 390 565 470 525 539 L1200 539 L1200 0 Z" fill="#7a7a7a"/>
  </svg>
  <h2 class="services-title">OUR SERVICES</h2>
  <div class="rule" style="left:660px; top:136px; width:56px; background:#ffffff;"></div>
  <ul class="service-list">
    <li><svg width="18" height="18" viewBox="0 0 18 18"><path d="M15 9 A6 6 0 1 1 11.5 3.5" fill="none" stroke="#fff" stroke-width="1.5"/><path d="M5.5 8.5 L8.5 11.5 L16 4" fill="none" stroke="#fff" stroke-width="1.6"/></svg>Concept Origination and Project Management</li>
    <li><svg width="18" height="18" viewBox="0 0 18 18"><path d="M15 9 A6 6 0 1 1 11.5 3.5" fill="none" stroke="#fff" stroke-width="1.5"/><path d="M5.5 8.5 L8.5 11.5 L16 4" fill="none" stroke="#fff" stroke-width="1.6"/></svg>Review of Proposed Plans for New Construction and Remodels</li>
    <li><svg width="18" height="18" viewBox="0 0 18 18"><path d="M15 9 A6 6 0 1 1 11.5 3.5" fill="none" stroke="#fff" stroke-width="1.5"/><path d="M5.5 8.5 L8.5 11.5 L16 4" fill="none" stroke="#fff" stroke-width="1.6"/></svg>Procurement of Furniture, Accents, Art, Fixtures and Fittings</li>
    <li><svg width="18" height="18" viewBox="0 0 18 18"><path d="M15 9 A6 6 0 1 1 11.5 3.5" fill="none" stroke="#fff" stroke-width="1.5"/><path d="M5.5 8.5 L8.5 11.5 L16 4" fill="none" stroke="#fff" stroke-width="1.6"/></svg>Selection of Paints, Finishes and Construction Materials</li>
    <li><svg width="18" height="18" viewBox="0 0 18 18"><path d="M15 9 A6 6 0 1 1 11.5 3.5" fill="none" stroke="#fff" stroke-width="1.5"/><path d="M5.5 8.5 L8.5 11.5 L16 4" fill="none" stroke="#fff" stroke-width="1.6"/></svg>Vendor Coordination and Recommendations</li>
    <li><svg width="18" height="18" viewBox="0 0 18 18"><path d="M15 9 A6 6 0 1 1 11.5 3.5" fill="none" stroke="#fff" stroke-width="1.5"/><path d="M5.5 8.5 L8.5 11.5 L16 4" fill="none" stroke="#fff" stroke-width="1.6"/></svg>Home Staging, Styling and Editing</li>
  </ul>
</section>

<section class="gallery">
  <h2 class="gallery-title"><span class="light">OUR</span> GALLERY</h2>
  <div class="rule" style="left:572px; top:1859px; width:48px;"></div>
  <div class="gallery-grid">
    <div class="tile" role="img" aria-label="Brick patio with black awning and outdoor seating" style="background:linear-gradient(160deg,#3a3a3a,#8a6e5a 60%,#d6d2c8)"></div>
    <div class="tile" role="img" aria-label="Covered outdoor lounge with wicker seating" style="background:linear-gradient(180deg,#e8e6e2,#9c8a7c 55%,#8a8f76)"></div>
    <div class="tile" role="img" aria-label="White dining table with modern chairs" style="background:linear-gradient(160deg,#c9c9c7,#f1f1f0 60%,#d8d8d6)"></div>
    <div class="tile" role="img" aria-label="White stair hall with sculpture" style="background:linear-gradient(120deg,#dcdcda,#f6f6f5 60%,#c8c8c6)"></div>
    <div class="tile" role="img" aria-label="Grey sofa and ottoman in a bright room" style="background:linear-gradient(180deg,#eeeeec,#a8a9a8 55%,#d9cfc2)"></div>
    <div class="tile" role="img" aria-label="Curved sofa beside a round table" style="background:linear-gradient(160deg,#d5cfc6,#ebe5dc 55%,#b9b0a4)"></div>
    <div class="tile" role="img" aria-label="Library sitting room with fireplace and glass table" style="background:linear-gradient(160deg,#4e4e50,#8a8c90 50%,#b3b1ae)"></div>
    <div class="tile" role="img" aria-label="Dining area with gilded mirror and lantern" style="background:linear-gradient(160deg,#a88a5e,#efe8dc 55%,#8c6c46)"></div>
    <div class="tile" role="img" aria-label="Living room with cream sofa and wall art" style="background:linear-gradient(160deg,#b9ad98,#ece6dc 55%,#9a8466)"></div>
    <div class="tile" role="img" aria-label="Wooden dining table with candelabra" style="background:linear-gradient(160deg,#d9d6cf,#8a5c36 60%,#c9c4ba)"></div>
    <div class="tile" role="img" aria-label="Colourful painted surface" style="background:linear-gradient(160deg,#c8b07a,#d65a8c 50%,#b44a6a)"></div>
    <div class="tile" role="img" aria-label="Open stair beside a kitchen bar" style="background:linear-gradient(160deg,#3e3a36,#e9e6e0 55%,#c4b49a)"></div>
  </div>
  <div class="btn-outline">VIEW MORE</div>
</section>

<section class="contact" role="img" aria-label="Darkened living room with staircase and rug"></section>
<h2 class="contact-title">CONTACT US</h2>
<div class="rule" style="left:573px; top:2745px; width:54px; background:#ffffff;"></div>
<div class="field" style="left:214px; top:2771px; width:380px; height:50px;">First Name*</div>
<div class="field" style="left:607px; top:2771px; width:382px; height:50px;">Last Name*</div>
<div class="field" style="left:214px; top:2836px; width:380px; height:50px;">Email address*</div>
<div class="field" style="left:607px; top:2836px; width:382px; height:50px;">Phone*</div>
<div class="field" style="left:216px; top:2902px; width:773px; height:126px;">Message</div>
<div class="btn-submit">SUBMIT</div>

<footer class="site-footer">
  <nav class="footer-nav">
    <a style="left:271px">HOME</a>
    <a style="left:397px">ABOUT US</a>
    <a style="left:552px">SERVICES</a>
    <a style="left:702px">GALLERY</a>
    <a style="left:846px">CONTACT</a>
  </nav>
  <p class="copyright">© 2020 Rosa Lynn Thackery | All Rights Reserved</p>
  <span class="social" style="left:533px"></span>
  <span class="social" style="left:578px"></span>
  <span class="social" style="left:623px"></span>
</footer>

</body>
</html>
```